Biz Cards

Please design new business cards. The colors are black and white
Updates

I'm in a meeting all day and will look at all these options tomorrow.

Industry/Entity Type

Flexible Office Space

Contact Information for Business Card

add the tag line- "Upgrade your workday."

Colors

Designer to choose only greyscale colors for use in the design.

Requirements
Must have
• Logo, contact name, phone number, email, website on one side. Upgrade your workday. QR code to website on the other side.

```html
<!DOCTYPE html>
<html lang="en">
<head>
<meta charset="utf-8">
<title>Vanta Private Offices – Business Cards</title>
<link href="https://fonts.googleapis.com/css2?family=Montserrat:wght@400;600;700&display=swap" rel="stylesheet">
<style>
  :root {
    --backdrop: #2b2b2b;
    --card: #1f1f20;
    --card-edge: #262627;
    --ink: #f2f2f2;
    --ink-soft: #d6d6d6;
    --logo-front: #6a6a6a;
  }
  * { margin: 0; padding: 0; box-sizing: border-box; }
  html, body { width: 1200px; height: 1138px; overflow: hidden; }
  body {
    background: var(--backdrop);
    font-family: "Montserrat", sans-serif;
    color: var(--ink);
    position: relative;
  }
  .card {
    position: absolute;
    border-radius: 16px;
    background: linear-gradient(160deg, var(--card) 0%, var(--card-edge) 100%);
  }
  .card--front { left: 274px; top: 186px; width: 623px; height: 376px; }
  .card--back  { left: 276px; top: 608px; width: 618px; height: 374px; }

  .front-wordmark {
    position: absolute;
    left: 0; right: 0; top: 160px;
    text-align: center;
    font-weight: 700;
    font-size: 28px;
    letter-spacing: 2px;
    color: var(--logo-front);
  }
  .tagline {
    position: absolute;
    left: 0; right: 0; top: 327px;
    text-align: center;
    font-weight: 600;
    font-size: 15px;
    letter-spacing: 0.6px;
    color: var(--ink-soft);
  }

  .person { position: absolute; left: 46px; top: 52px; }
  .person__name { font-weight: 700; font-size: 26px; letter-spacing: 0.3px; line-height: 1.1; }
  .person__role { font-weight: 400; font-size: 15.5px; color: var(--ink-soft); margin-top: 2px; }

  .address {
    position: absolute; left: 46px; top: 204px;
    font-size: 15px; line-height: 24px; color: var(--ink-soft);
  }
  .contacts {
    position: absolute; left: 46px; top: 258px;
    list-style: none;
  }
  .contacts li {
    display: flex; align-items: center;
    height: 24px; font-size: 15px; color: var(--ink-soft);
  }
  .contacts svg { width: 15px; height: 15px; margin-right: 17px; fill: var(--ink-soft); }

  .back-wordmark {
    position: absolute; right: 44px; top: 282px;
    font-weight: 700; font-size: 18px; letter-spacing: 1px;
    color: var(--ink); white-space: nowrap;
  }
</style>
</head>
<body>
  <section class="card card--front">
    <div class="front-wordmark">VANTA PRIVATE OFFICES</div>
    <p class="tagline">UPGRADE YOUR WORKDAY</p>
  </section>

  <section class="card card--back">
    <div class="person">
      <h1 class="person__name">NORA VALE</h1>
      <p class="person__role">Managing Director</p>
    </div>

    <p class="address">123 Anywhere, Any City,<br>Any Town, US 012345</p>

    <ul class="contacts">
      <li>
        <svg viewBox="0 0 16 16" aria-hidden="true"><path d="M2 5c0-2 2-3 6-3s6 1 6 3v1h-3V5H5v1H2z"/><rect x="3" y="7" width="10" height="7" rx="1"/></svg>
        000-0000-000
      </li>
      <li>
        <svg viewBox="0 0 16 16" aria-hidden="true"><path d="M1 3h14v10H1z M2 4l6 5 6-5" fill="none" stroke="#d6d6d6" stroke-width="1.6"/></svg>
        sale@vantaoffices.com
      </li>
      <li>
        <svg viewBox="0 0 16 16" aria-hidden="true"><g fill="none" stroke="#d6d6d6" stroke-width="1.3"><circle cx="8" cy="8" r="6.5"/><ellipse cx="8" cy="8" rx="3" ry="6.5"/><path d="M1.5 8h13M2.5 4.5h11M2.5 11.5h11"/></g></svg>
        www.vantaoffices.com
      </li>
    </ul>

    <div class="back-wordmark">VANTA PRIVATE OFFICES</div>
  </section>
</body>
</html>
```